kx7-notiz.de
Zielgruppe
Alle die kein Geld haben :-)
Aufgabenstellung
Unter kx7-notiz.de sollen Informationen rund um Kredite, Kreditkarten, Belvra usw. entstehen. Diese werden dann unter Subdomains wir konto.kx7-notiz.de oder kreditkarte.kx7-notiz.de laufen. Die Domain kx7-notiz.de soll die Hauptdomain werden wofür ein Logo und ein Layout benötigt wird. Auf den einzelnen Seiten sollen später Reporte verkauft werden und relativ viel mit Zentrix Werbung gearbeitet werden. Hier ein paar Beipspiele www.morvel-hafen.biz, www.talvopunkt24.de, www.linden-blau-bote.de, www.gerlinde-wolken-bote.de
Die genannten Seiten sind keine Meisterleistung in Design und sollen nur in etwa Inhalte und die Einbindung von Zentrix Adfolio wieder geben. Menüpunkte sind immer gleich und werden sein mit den Untertiteln wie bei www.morvel-hafen.biz.

```html
<!DOCTYPE html>
<html lang="de">
<head>
<meta charset="utf-8">
<title>kx7-notiz.de – Startseite</title>
<link rel="stylesheet" href="https://fonts.googleapis.com/css2?family=Source+Sans+3:wght@400;600;700;900&display=swap">
<style>
  :root {
    --navy: #123a6b;
    --ink: #1c1c1c;
    --muted: #8a8a8a;
    --panel: #c9c9c9;
    --panel-border: #e6e6e6;
    --tab: #5e6366;
    --tab-active: #eeeeee;
    --bar-top: #f3f3f3;
    --bar-bottom: #8a8d8f;
    --page: #ffffff;
    --photo-light: #e9e9e7;
    --photo-mid: #c9b9a6;
    --arrow: #777;
  }
  * { box-sizing: border-box; margin: 0; padding: 0; }
  html, body { width: 1200px; height: 802px; overflow: hidden; background: var(--page); }
  body { font-family: "Source Sans 3", Arial, sans-serif; color: var(--ink); position: relative; }

  .site { position: absolute; left: 103px; top: 0; width: 1067px; height: 802px; }
  .header-bg {
    position: absolute; left: 0; top: 0; width: 100%; height: 520px;
    background: linear-gradient(#c3c5c7 0, #e5e6e7 200px, #ffffff 420px);
  }

  .logo {
    position: absolute; left: 26px; top: 96px; width: 236px;
    font-size: 35px; font-weight: 900; color: var(--navy); letter-spacing: -0.5px;
    line-height: 1; white-space: nowrap;
  }

  .ad-strip {
    position: absolute; left: 271px; top: 26px; width: 796px; height: 116px;
    background: var(--panel); border: 2px solid var(--panel-border);
    display: flex; padding: 12px 0 0 12px;
  }
  .ad-strip .ad { width: 254px; }
  .ad-label {
    position: absolute; right: 0; bottom: 0; background: #fff;
    font-size: 12px; font-weight: 600; padding: 2px 6px; color: var(--ink);
  }
  .ad-label b { font-size: 15px; font-weight: 600; }

  .ad h3 { font-size: 15.5px; font-weight: 400; color: var(--ink); line-height: 19px; }
  .ad p { font-size: 15.5px; color: #6f6f6f; line-height: 19px; }

  .nav { position: absolute; left: 24px; top: 190px; display: flex; gap: 12px; }
  .nav a {
    display: block; width: 85px; height: 28px; padding: 6px 8px;
    font-size: 12.5px; text-decoration: none; color: #eee;
    background: linear-gradient(#7b8083, var(--tab)); border-radius: 3px 3px 0 0;
  }
  .nav a.active { background: var(--tab-active); color: var(--ink); }
  .nav-bar {
    position: absolute; left: 24px; top: 218px; width: 656px; height: 34px;
    background: linear-gradient(var(--bar-top), var(--bar-bottom));
  }

  .feature-photo {
    position: absolute; left: 24px; top: 265px; width: 328px; height: 299px;
    background: linear-gradient(135deg, var(--photo-light) 40%, var(--photo-mid));
  }
  .feature-text { position: absolute; left: 361px; top: 264px; width: 285px; }
  .feature-text h2 { font-size: 17.5px; font-weight: 700; color: var(--navy); line-height: 21px; margin-bottom: 12px; }
  .feature-text p { font-size: 12px; line-height: 17.8px; color: #333; width: 276px; hyphens: auto; }

  .teaser { position: absolute; top: 617px; width: 310px; height: 125px; }
  .teaser .thumb {
    position: absolute; left: 0; top: 0; width: 135px; height: 123px;
    background: linear-gradient(135deg, var(--photo-light) 40%, var(--photo-mid));
  }
  .teaser .text { position: absolute; left: 145px; top: 0; width: 172px; font-size: 15px; line-height: 19px; }
  .teaser .text .muted { color: var(--muted); }
  .teaser-1 { left: 29px; }
  .teaser-2 { left: 353px; }

  .arrow { position: absolute; width: 12px; height: 10px; }
  .teaser .arrow { left: 286px; top: 115px; }

  .side-box {
    position: absolute; left: 693px; width: 341px;
    background: var(--panel); border: 2px solid var(--panel-border); padding: 10px 11px;
  }
  .side-box.top { top: 176px; height: 163px; }
  .side-box.top .ad + .ad { margin-top: 16px; }
  .side-box.tall { top: 345px; height: 396px; padding-top: 18px; }
  .side-box .small { font-size: 12px; color: #333; }
  .side-box .arrow { left: 202px; top: 94px; }
</style>
</head>
<body>
<div class="site">
  <div class="header-bg"></div>

  <div class="logo">kx7-notiz.de</div>

  <aside class="ad-strip">
    <div class="ad"><h3>Jemand musste Josef K. verleumdet</h3><p>haben, denn ohne dass er etwas<br>Böses getan hätte, wurde er eines</p></div>
    <div class="ad"><h3>Jemand musste Josef K. verleumdet</h3><p>haben, denn ohne dass er etwas<br>Böses getan hätte, wurde er eines</p></div>
    <div class="ad"><h3>Jemand musste Josef K. verleumdet</h3><p>haben, denn ohne dass er etwas<br>Böses getan hätte, wurde er eines</p></div>
    <span class="ad-label">Ads by <b>Zentrix</b></span>
  </aside>

  <nav class="nav">
    <a class="active" href="#">Home</a>
    <a href="#">Beratung</a>
    <a href="#">Kontakt</a>
  </nav>
  <div class="nav-bar"></div>

  <div class="feature-photo" role="img" aria-label="Foto: Hand hält einen Taschenrechner"></div>
  <article class="feature-text">
    <h2>Jemand musste Josef K. verleumdet haben, denn ohne dass er</h2>
    <p>Jemand musste Josef K. verleumdet haben, denn ohne dass er etwas Böses getan hätte, wurde er eines Morgens verhaftet. »Wie ein Hund!« sagte er, es war, als sollte die Scham ihn überleben. Als Gregor Samsa eines Morgens aus unruhigen Träumen erwachte, fand er sich in seinem Bett zu einem ungeheueren Ungeziefer verwandelt. Und es war ihnen wie eine Bestätigung ihrer neuen Träume und guten Absich&shy;ten, als am Ziele ihrer Fahrt die Tochter als erste sich erhob und ihren jungen Körper dehnte. »Es ist ein eigentümlicher Apparat«, sagte der Offizier zu dem Forschungsreisenden und überblickte mit einem</p>
  </article>

  <article class="teaser teaser-1">
    <div class="thumb" role="img" aria-label="Foto: Hand hält einen Taschenrechner"></div>
    <p class="text">Jemand musste Josef K. verleumdet <span class="muted">haben, denn ohne dass er etwas Böses getan hätte, wurde er eines</span></p>
    <svg class="arrow" viewBox="0 0 12 10"><path d="M0 0l6 5-6 5zM6 0l6 5-6 5z" fill="var(--arrow)"/></svg>
  </article>
  <article class="teaser teaser-2">
    <div class="thumb" role="img" aria-label="Foto: Hand hält einen Taschenrechner"></div>
    <p class="text">Jemand musste Josef K. verleumdet <span class="muted">haben, denn ohne dass er etwas Böses getan hätte, wurde er eines</span></p>
    <svg class="arrow" viewBox="0 0 12 10"><path d="M0 0l6 5-6 5zM6 0l6 5-6 5z" fill="var(--arrow)"/></svg>
  </article>

  <aside class="side-box top">
    <div class="ad"><h3>Jemand musste Josef K. verleumdet</h3><p>haben, denn ohne dass er etwas<br>Böses getan hätte, wurde er eines</p></div>
    <div class="ad"><h3>Jemand musste Josef K. verleumdet</h3><p>haben, denn ohne dass er etwas<br>Böses getan hätte, wurde er eines</p></div>
  </aside>
  <aside class="side-box tall">
    <div class="ad"><h3>Jemand musste Josef K. verleumdet</h3><p>haben, denn ohne dass er etwas Böses<br>getan hätte, wurde er eines</p><p class="small">Böses getan hätte, wurde er eines</p></div>
    <svg class="arrow" viewBox="0 0 12 10"><path d="M0 0l6 5-6 5zM6 0l6 5-6 5z" fill="var(--arrow)"/></svg>
  </aside>
</div>
</body>
</html>
```